Roofing Contractor business card redesign

I want to redesign my business card with a fresh, eye catching concept

Target Market(s)

Residential Roofing Clients, potential employees, and subcontractors.

Industry/Entity Type

Business

Colors

Designer to choose colors to be used in the design.

Requirements
Nice to have
• I just want something that's more pleasing to the eye. You can use a combination of either / or of my logos.

```html
<!DOCTYPE html>
<html lang="en">
<head>
<meta charset="utf-8">
<title>Steady Crew General Contractors — Business Card</title>
<link rel="stylesheet" href="https://fonts.googleapis.com/css2?family=Roboto+Condensed:wght@700&family=Source+Sans+3:wght@800&display=swap">
<style>
  :root {
    --yellow: #fdcb0e;
    --yellow-deep: #f2b90a;
    --brown: #3d1f1f;
    --orange: #e06b20;
    --backdrop-center: #4a4a4a;
    --backdrop-edge: #161616;
    --name-font: "Roboto Condensed", Arial Narrow, sans-serif;
    --sub-font: "Source Sans 3", Arial, sans-serif;
  }
  * { margin: 0; padding: 0; box-sizing: border-box; }
  html, body {
    width: 1189px; height: 1200px; overflow: hidden;
  }
  body {
    position: relative;
    background: radial-gradient(ellipse at 50% 50%, var(--backdrop-center) 0%, #2a2a2a 55%, var(--backdrop-edge) 100%);
  }
  .card {
    position: absolute;
    left: 170px;
    width: 857px;
    height: 490px;
    background: var(--yellow);
    overflow: hidden;
    box-shadow: 0 6px 14px rgba(0,0,0,0.55);
  }
  .card--front {
    top: 66px;
    border-radius: 49px 0 65px 0;
  }
  .card--back {
    top: 625px;
    border-radius: 0 49px 0 65px;
  }
  .brand {
    position: absolute;
    display: flex;
    align-items: center;
    color: var(--brown);
    font-family: var(--name-font);
    font-weight: 700;
    line-height: 1;
    white-space: nowrap;
  }
  .brand__dot {
    border-radius: 50%;
    background: var(--brown);
    flex: none;
  }
  .subtitle {
    position: absolute;
    color: var(--brown);
    font-family: var(--sub-font);
    font-weight: 800;
    white-space: nowrap;
    text-shadow: 0 0 2px #fff, 1px 2px 2px rgba(0,0,0,0.3);
  }
  .card--front .brand { left: 160px; top: 205px; font-size: 96px; gap: 18px; }
  .card--front .brand__dot { width: 92px; height: 92px; }
  .card--front .subtitle { left: 165px; top: 362px; font-size: 41px; letter-spacing: -0.5px; }

  .card--back .brand { left: 44px; top: 118px; font-size: 70px; gap: 12px; }
  .card--back .brand__dot { width: 66px; height: 66px; }
  .card--back .subtitle { left: 45px; top: 226px; font-size: 28px; letter-spacing: -0.4px; }

  .contact {
    position: absolute;
    left: 43px;
    top: 270px;
    color: var(--brown);
    font-family: var(--name-font);
    font-weight: 700;
    text-shadow: 0 0 2px #fff, 1px 2px 2px rgba(0,0,0,0.3);
  }
  .contact__phone { font-size: 42px; line-height: 1.2; }
  .contact__tagline { font-size: 26px; margin-top: 8px; transform: scaleX(0.9); transform-origin: left; }

  .band { position: absolute; left: 0; top: 0; width: 857px; height: 490px; }
  .crew-art {
    position: absolute;
    left: 490px;
    top: 165px;
    width: 367px;
    height: 325px;
    border-radius: 120px 0 0 0;
    background: linear-gradient(160deg, var(--yellow-deep) 0%, var(--orange) 55%, var(--brown) 100%);
  }
  .website {
    position: absolute;
    left: 238px;
    top: 418px;
    color: var(--yellow);
    font-family: var(--name-font);
    font-weight: 700;
    font-size: 34px;
    letter-spacing: -0.5px;
  }
</style>
</head>
<body>
  <section class="card card--front" aria-label="Card front">
    <div class="brand">
      <span>Steady</span>
      <span class="brand__dot" aria-hidden="true"></span>
      <span>Crew</span>
    </div>
    <p class="subtitle">General Contractors, Inc.</p>
  </section>

  <section class="card card--back" aria-label="Card back">
    <svg class="band" viewBox="0 0 857 490" aria-hidden="true">
      <path d="M0 462 Q 300 385 857 395 L857 490 L0 490 Z" fill="var(--brown)"/>
    </svg>
    <div class="crew-art" role="img" aria-label="Illustration of three roofing workers with tools, arms crossed"></div>
    <div class="brand">
      <span>Steady</span>
      <span class="brand__dot" aria-hidden="true"></span>
      <span>Crew</span>
    </div>
    <p class="subtitle">General Contractors, Inc.</p>
    <div class="contact">
      <p class="contact__phone">(555) 014 - 2290</p>
      <p class="contact__tagline">Quality Roofing, Installed by Hand</p>
    </div>
    <p class="website">SteadyCrewGC.com</p>
  </section>
</body>
</html>
```